International game business needs app design

We are planning to release a new mobile game on Zarn9 which requires a fresh, flat, reduced and functional design, fulfilling Brindle’s Zarn9 design guidelines
.
The design shall be created for a dashboard, where players should be able to pick levels (icon + short description; 300+ levels), opponents (icon/photo/avatar image + short description; 5-100) and read/delete system/chat messages (icon, 2-3 actions (delete, accept/decline), text with up to 500 characters; 1-100 entries), Menu bar (settings, shop, leaderboards, achievements, and one or two more menu items) It must consider means to search/select levels and opponents. Would be nice to have an option to start playing immediately (with a random opponent on a random level)

Overall Style/Look: fresh, flat, functional, lot’s of free space, warm color scheme. If full screen images are being used it must be considered that there are user-generated photos or avatars which have to work with it in combination

Ideally the design is responsive and would work both on a smartphone and a tablet. Smartphone is top priority, tablet is optional.

The app will be a game for women predominantly, aged 25-35, with higher education and household net income, which should be reflected in color scheme, icons and navigation.

Some of us like flat design, so you might stick to that or impress all of us with something completely new!

The winner will have the chance to design all screens for the app and will have access to a much bigger budget.

UPDATE: A wireframe is attached - but you don't have to follow the depicted layout. Actually it would be highly appreciated if you could come up with something new. The only important thing is that all the listed components must appear somehow on the dashboard.

Target Market(s)

US, AU, NZ, GB, CA

Industry/Entity Type

Education

Colors

Designer to choose colors to be used in the design.

Requirements
Must have
• All the functional components described above.
Design must be in line with Zarn9 design guidelines https://builders.brindlecore.net/library/zarn/documentation/ViewerJourney/Outline/HandheldGuide/index.html
Nice to have
• We would like to have someone with the following attributes:
* minimum 5 zarn design in your past at least 2 of them responsive – please provide links to the apps you created
* besides UI designer skills would be nice you to have UX skills

The most important factors for us are quality, creativity, speed, flexibility (“be able to take criticism into account”)
Should not have
• We don’t want a girly design so please don’t use too much pinks, flowers and such. The design should be acceptable by men too.

```html
<!DOCTYPE html>
<html lang="en">
<head>
<meta charset="utf-8">
<title>Game Dashboard</title>
<link href="https://fonts.googleapis.com/css2?family=Open+Sans:wght@400;600;700&display=swap" rel="stylesheet">
<style>
:root{
  --page:#dfeef7;
  --status:#707079;
  --nav:#4b4868;
  --nav-icon:#8d8aa6;
  --tile:#4d4a6c;
  --accent:#f5476a;
  --light:#ececef;
  --panel:#ffffff;
  --row:#e5e5e8;
  --row-text:#9a9aa2;
  --name-text:#7b7b84;
  --title:#5b5780;
  --muted:#a7a7ae;
  --white:#ffffff;
}
*{box-sizing:border-box;margin:0;padding:0}
html,body{width:834px;height:1200px;overflow:hidden}
body{background:var(--page);font-family:"Open Sans",Arial,sans-serif;position:relative}
.screen{position:absolute;left:83px;top:4px;width:522px;height:931px;transform:scale(1.28);transform-origin:0 0;background:var(--light);overflow:hidden}
.status-bar{height:28px;background:var(--status);color:var(--white);font-weight:700;font-size:19px;display:flex;align-items:center;justify-content:space-between;padding:0 8px;line-height:1}
.status-bar .carrier{display:flex;align-items:flex-end;gap:4px}
.signal{display:flex;align-items:flex-end;gap:2px;height:14px}
.signal i{display:block;width:3px;background:var(--white)}
.status-bar .right{display:flex;align-items:center;gap:6px}
.nav-bar{height:52px;background:var(--nav);position:relative}
.nav-bar svg{position:absolute;top:14px}
.tabs{position:absolute;top:92px;left:0;width:100%;display:flex;justify-content:center;gap:12px}
.tab{height:18px;border-radius:5px;background:#cfcfd4;color:var(--white);font-size:8px;display:flex;align-items:center;justify-content:center;width:78px}
.tab.active{background:var(--accent)}
.levels{position:absolute;top:132px;left:43px;display:grid;grid-template-columns:repeat(4,99px);grid-auto-rows:68px;column-gap:15px;row-gap:12px}
.level{background:var(--tile);border-radius:4px;color:var(--white);text-align:center;padding-top:6px}
.level.featured{background:var(--accent)}
.level .name{font-size:10px;line-height:12px}
.level .num{font-size:22px;font-weight:700;line-height:26px}
.level .lbl{font-size:11px;line-height:14px}
.pager{position:absolute;top:186px;font-size:22px;color:#8f8fa0;font-weight:400}
.search{position:absolute;top:297px;left:17px;width:482px;height:33px;background:var(--white);border-radius:4px;color:var(--muted);font-size:14px;display:flex;align-items:center;justify-content:center}
.search svg{position:absolute;right:14px;top:7px}
.opponents{position:absolute;top:345px;left:0;width:522px;height:192px;background:linear-gradient(90deg,#d9c9c6 0%,#cdbdc4 25%,#c9c2cc 50%,#d4c6c6 75%,#c8c4d0 100%)}
.opponent{position:absolute;top:20px;width:124px;text-align:center}
.avatar{width:122px;height:122px;border-radius:50%;border:4px solid var(--white);margin:0 auto}
.opponent .name{position:relative;margin:-18px auto 0;width:100px;height:20px;border-radius:10px;background:var(--white);font-size:12px;color:#555;line-height:20px}
.opponent .actions{display:flex;justify-content:center;gap:12px;margin-top:12px}
.lower{position:absolute;top:537px;left:0;width:522px;height:394px;background:#efeff1}
.panel{position:absolute;top:20px;width:246px;height:278px;background:var(--panel)}
.panel.messages{left:7px}
.panel.notifications{left:268px}
.panel-head{height:44px;display:flex;align-items:center;gap:10px;padding-left:16px;color:var(--title);font-size:15px}
.close{position:absolute;right:8px;top:10px;width:16px;height:16px;background:#bdbdc3;color:var(--white);font-size:10px;line-height:16px;text-align:center}
.msg-list{list-style:none;padding:5px 8px 0}
.msg{height:22px;margin-bottom:10.3px;background:var(--row);border-radius:3px;display:flex;align-items:center;padding:0 7px 0 14px;font-size:9px;color:var(--row-text)}
.msg svg{margin-right:18px}
.msg .from{flex:1}
.msg .who{font-size:13px;color:var(--name-text);font-weight:600}
.msg.selected{background:var(--tile);color:var(--white)}
.msg.selected .who{color:var(--white)}
.note-list{list-style:none;padding:12px 0 0 10px}
.note{display:flex;align-items:center;gap:14px;height:55px}
.note .face{width:31px;height:31px;border-radius:50%;flex:none}
.note p{font-size:10.5px;color:var(--muted);line-height:13px;width:172px}
.note b{font-weight:400;color:var(--accent)}
.play{position:absolute;top:319px;left:35px;width:445px;height:54px;background:var(--accent);border-radius:3px;color:var(--white);font-size:21px;font-weight:600;display:flex;align-items:center;justify-content:center}
</style>
</head>
<body>
<main class="screen">
  <div class="status-bar">
    <div class="carrier"><span class="signal"><i style="height:5px"></i><i style="height:7px"></i><i style="height:9px"></i><i style="height:12px"></i><i style="height:14px"></i></span>DINE</div>
    <div class="time">10:35 AM</div>
    <div class="right">
      <svg width="16" height="16" viewBox="0 0 16 16"><circle cx="8" cy="8" r="8" fill="#fff"/><path d="M8 3v5h4" stroke="#707079" stroke-width="2" fill="none"/></svg>
      <span>65%</span>
      <svg width="34" height="16" viewBox="0 0 34 16"><rect x="1" y="2" width="28" height="12" fill="none" stroke="#fff" stroke-width="1.5"/><rect x="3" y="4" width="17" height="8" fill="#fff"/><rect x="30" y="6" width="3" height="4" fill="#fff"/></svg>
    </div>
  </div>

  <nav class="nav-bar" aria-label="Main menu">
    <svg style="left:76px" width="24" height="24" viewBox="0 0 24 24" aria-label="Settings"><circle cx="12" cy="12" r="7" fill="none" stroke="var(--nav-icon)" stroke-width="4" stroke-dasharray="3 2.5"/><circle cx="12" cy="12" r="5" fill="none" stroke="var(--nav-icon)" stroke-width="2.5"/></svg>
    <svg style="left:192px" width="26" height="24" viewBox="0 0 26 24" aria-label="Shop"><path d="M1 3h4l3 12h13l3-9H7" fill="none" stroke="var(--nav-icon)" stroke-width="2.5"/><rect x="12.5" y="6" width="2.5" height="5" fill="var(--nav-icon)"/><circle cx="10" cy="20" r="2" fill="var(--nav-icon)"/><circle cx="19" cy="20" r="2" fill="var(--nav-icon)"/></svg>
    <svg style="left:318px" width="22" height="26" viewBox="0 0 22 26" aria-label="Leaderboards"><path d="M2 1h12l6 6v18H2z" fill="none" stroke="var(--nav-icon)" stroke-width="2"/><path d="M6 11h10M6 15h10M6 19h10" stroke="var(--nav-icon)" stroke-width="2"/></svg>
    <svg style="left:425px" width="24" height="24" viewBox="0 0 24 24" aria-label="Achievements"><circle cx="12" cy="11" r="5" fill="var(--nav-icon)"/><rect x="9.5" y="16" width="5" height="4" fill="var(--nav-icon)"/><path d="M12 1v3M3 11h3M18 11h3M5 4l2 2M19 4l-2 2" stroke="var(--nav-icon)" stroke-width="2"/></svg>
  </nav>

  <div class="tabs">
    <div class="tab">RECENT LEVELS</div>
    <div class="tab active">CHOOSE LEVEL</div>
    <div class="tab">RANDOM</div>
  </div>

  <span class="pager" style="left:14px">&lsaquo;</span>
  <span class="pager" style="left:498px">&rsaquo;</span>

  <section class="levels" aria-label="Levels">
    <div class="level featured"><div class="name">Hipster wardrobe</div><div class="num">15</div><div class="lbl">LEVEL</div></div>
    <div class="level"><div class="name">Scribble</div><div class="num">8</div><div class="lbl">LEVEL</div></div>
    <div class="level"><div class="name">Castle dash</div><div class="num">3</div><div class="lbl">LEVEL</div></div>
    <div class="level"><div class="name">Morphing tool</div><div class="num">11</div><div class="lbl">LEVEL</div></div>
    <div class="level featured"><div class="name">Hipster wardrobe</div><div class="num">15</div><div class="lbl">LEVEL</div></div>
    <div class="level"><div class="name">Scribble</div><div class="num">8</div><div class="lbl">LEVEL</div></div>
    <div class="level"><div class="name">Castle dash</div><div class="num">3</div><div class="lbl">LEVEL</div></div>
    <div class="level"><div class="name">Morphing tool</div><div class="num">11</div><div class="lbl">LEVEL</div></div>
  </section>

  <div class="search">search opponent
    <svg width="20" height="20" viewBox="0 0 20 20"><circle cx="8" cy="8" r="6.5" fill="none" stroke="#c5c5cb" stroke-width="1.5"/><path d="M13 13l6 6" stroke="#c5c5cb" stroke-width="1.5"/></svg>
  </div>

  <section class="opponents" role="img" aria-label="Soft blurred backdrop behind opponent photos">
    <div class="opponent" style="left:28px">
      <div class="avatar" role="img" aria-label="Profile photo of Sophia Price" style="background:linear-gradient(160deg,#b89a86,#6b4a3c)"></div>
      <div class="name">Sophia Price</div>
      <div class="actions">
        <svg width="20" height="18" viewBox="0 0 20 18"><path d="M10 0l3 6 7 1-5 5 1 6-6-3-6 3 1-6-5-5 7-1z" fill="#fff"/></svg>
        <svg width="20" height="18" viewBox="0 0 20 18"><path d="M10 18L2 10a5 5 0 0 1 8-7 5 5 0 0 1 8 7z" fill="var(--accent)"/></svg>
        <svg width="20" height="18" viewBox="0 0 20 18"><path d="M1 1h18v12H8l-4 4v-4H1z" fill="#fff"/></svg>
      </div>
    </div>
    <div class="opponent" style="left:198px">
      <div class="avatar" role="img" aria-label="Profile photo of Jack X" style="background:linear-gradient(160deg,#a9a39c,#5a504a)"></div>
      <div class="name">Jack X</div>
      <div class="actions">
        <svg width="20" height="18" viewBox="0 0 20 18"><path d="M10 0l3 6 7 1-5 5 1 6-6-3-6 3 1-6-5-5 7-1z" fill="#fff"/></svg>
        <svg width="20" height="18" viewBox="0 0 20 18"><path d="M10 18L2 10a5 5 0 0 1 8-7 5 5 0 0 1 8 7z" fill="#fff"/></svg>
        <svg width="20" height="18" viewBox="0 0 20 18"><path d="M1 1h18v12H8l-4 4v-4H1z" fill="#fff"/></svg>
      </div>
    </div>
    <div class="opponent" style="left:362px">
      <div class="avatar" role="img" aria-label="Profile photo of Lucy M" style="background:linear-gradient(160deg,#d8cfc8,#4e4444)"></div>
      <div class="name">Lucy M</div>
      <div class="actions">
        <svg width="20" height="18" viewBox="0 0 20 18"><path d="M10 0l3 6 7 1-5 5 1 6-6-3-6 3 1-6-5-5 7-1z" fill="#fff"/></svg>
        <svg width="20" height="18" viewBox="0 0 20 18"><path d="M10 18L2 10a5 5 0 0 1 8-7 5 5 0 0 1 8 7z" fill="#fff"/></svg>
        <svg width="20" height="18" viewBox="0 0 20 18"><path d="M1 1h18v12H8l-4 4v-4H1z" fill="#fff"/></svg>
      </div>
    </div>
  </section>

  <section class="lower">
    <div class="panel messages">
      <div class="panel-head">
        <svg width="30" height="26" viewBox="0 0 30 26"><path d="M2 2h16v11H8l-4 4v-4H2z" fill="var(--title)"/><path d="M11 9h17v11h-3v4l-4-4H11z" fill="none" stroke="var(--title)" stroke-width="2.5"/></svg>
        Messages
      </div>
      <div class="close">✕</div>
      <ul class="msg-list">
        <li class="msg"><svg width="20" height="13" viewBox="0 0 20 13"><rect x=".5" y=".5" width="19" height="12" fill="none" stroke="#fff"/><path d="M.5 .5l9.5 7 9.5-7" fill="none" stroke="#fff"/></svg><span class="from">message from</span><span class="who">Jack X</span></li>
        <li class="msg"><svg width="20" height="13" viewBox="0 0 20 13"><rect x=".5" y=".5" width="19" height="12" fill="none" stroke="#fff"/><path d="M.5 .5l9.5 7 9.5-7" fill="none" stroke="#fff"/></svg><span class="from">message from</span><span class="who">Sophia Price</span></li>
        <li class="msg selected"><svg width="20" height="13" viewBox="0 0 20 13"><rect x=".5" y=".5" width="19" height="12" fill="none" stroke="#fff"/><path d="M.5 .5l9.5 7 9.5-7" fill="none" stroke="#fff"/></svg><span class="from">message from</span><span class="who">Mark S</span></li>
        <li class="msg"><svg width="20" height="13" viewBox="0 0 20 13"><rect x=".5" y=".5" width="19" height="12" fill="none" stroke="#fff"/><path d="M.5 .5l9.5 7 9.5-7" fill="none" stroke="#fff"/></svg><span class="from">message from</span><span class="who">Ryan Sear</span></li>
        <li class="msg"><svg width="20" height="13" viewBox="0 0 20 13"><rect x=".5" y=".5" width="19" height="12" fill="none" stroke="#fff"/><path d="M.5 .5l9.5 7 9.5-7" fill="none" stroke="#fff"/></svg><span class="from">message from</span><span class="who">Jack X</span></li>
        <li class="msg"><svg width="20" height="13" viewBox="0 0 20 13"><rect x=".5" y=".5" width="19" height="12" fill="none" stroke="#fff"/><path d="M.5 .5l9.5 7 9.5-7" fill="none" stroke="#fff"/></svg><span class="from">message from</span><span class="who">Sophia Price</span></li>
        <li class="msg"><svg width="20" height="13" viewBox="0 0 20 13"><rect x=".5" y=".5" width="19" height="12" fill="none" stroke="#fff"/><path d="M.5 .5l9.5 7 9.5-7" fill="none" stroke="#fff"/></svg><span class="from">message from</span><span class="who">Ryan Sear</span></li>
      </ul>
    </div>

    <div class="panel notifications">
      <div class="panel-head">
        <svg width="22" height="26" viewBox="0 0 22 26"><rect x="1" y="1" width="2.5" height="24" fill="var(--title)"/><path d="M3.5 2h17l-4 6 4 6h-17z" fill="var(--title)"/></svg>
        Notifications
      </div>
      <div class="close">✕</div>
      <ul class="note-list">
        <li class="note"><span class="face" role="img" aria-label="Avatar of Amanda G" style="background:#d79a78"></span><p>Your friend <b>Amanda G</b> just played a game. Wanna try it too?</p></li>
        <li class="note"><span class="face" role="img" aria-label="Avatar of Stevie" style="background:#8a6a58"></span><p>Your friend <b>Stevie</b> just played a game. Wanna try it too?</p></li>
        <li class="note"><span class="face" role="img" aria-label="Avatar of Amanda G" style="background:#d79a78"></span><p>Your friend <b>Amanda G</b> just played a game. Wanna try it too?</p></li>
        <li class="note"><span class="face" role="img" aria-label="Avatar of Stevie" style="background:#8a6a58"></span><p>Your friend <b>Stevie</b> just played a game. Wanna try it too?</p></li>
      </ul>
    </div>

    <div class="play">Play a random game</div>
  </section>
</main>
</body>
</html>
```